Plakat-Design
Zielgruppe
wir produzieren mit verschiedenen Experten aus den Bereichen für 'Gesundheit, Nachhaltigkeit und Bewusstsein“
Onlinekurse für Endverbraucher.
Aufgabenstellung
Wir bauen ein Filmstudio in einer 'U' - Form
ich benötige ein 3-teiliges Design welches als Background zu unseren Videoaufnahmen dient.
vergleichen könnte man es mit einem InterviewStudio
es sollte ein schöne, neutraler Hintergrund sein, der für verschiedene Anlässe passt
Die Frage die Du Dir stellen solltest: 'wenn Du Deine Arbeit in einem Video erklären würdest, was soll hinter Dir zu sehen sein'
Am meisten gefiel mir bisher die Idee von einem intensiv-Farben-Frohen Verlauf.
Aber ich konnte mir das auch nicht ganz vorstellen bisher.
Ich wünsche mir einen modernen Hintergrund - aktuell habe ich 2 'echte' Steinwände - das Bild vom aktuellen Studio hänge ich mit an. (das Wissensfilm-Schule-Logo ist nicht mehr aktuell*) Jetzt möchte ich es moderner.
unser Brand ist BrightFold mit dem Logo laut Anhang.
unsere CI-Farben sind: blau: #01baff violett: #8200b2
muss aber nicht mit den Farben sein - kann auch was ganz freies sein...
Die Leinwände sind wie folg gross und werden von hinten beleuchtet:
links 3.00 Meter 3040 mm
mittig 4.50 Meter 4540 mm
rechts 5.00 Meter 5040 mm
Höhe: 3.10 Meter 3140 mm
für das Drucken der Banner gibt es folgende Vorgaben:
CMYK-Farbraum: ISO coated v2 (ECI)
250 dpi
zzgl. 20 mm Beschnitt umlaufend(siehe obigen mm-zahlen)
Stock-Bilder wenn möglich von BildVorrat, da habe ich noch grosses Kontingent übrig...
ich werde zum Vergleich mal etwas von einem TV-Sender hochladen...

```html
<!DOCTYPE html>
<html lang="de">
<head>
<meta charset="utf-8">
<title>BrightFold – Studio-Hintergrund, dreiteilig</title>
<link rel="stylesheet" href="https://fonts.googleapis.com/css2?family=Quicksand:wght@300&display=swap">
<style>
  :root {
    --page: #ffffff;
    --magenta-deep: #950862;
    --magenta-glow: #bd0c7d;
    --magenta-edge: #920760;
    --ornament-tint: rgba(196, 70, 150, 0.22);
    --logo-ink: #ffffff;
  }
  * { margin: 0; padding: 0; box-sizing: border-box; }
  html, body {
    width: 1200px;
    height: 849px;
    overflow: hidden;
    background: var(--page);
  }
  .sheet {
    position: relative;
    width: 1200px;
    height: 849px;
    background: var(--page);
  }
  .banner {
    position: absolute;
    top: 241px;
    height: 289px;
    overflow: hidden;
    background: var(--magenta-deep);
  }
  .banner--left   { left: 21px;  width: 281px; }
  .banner--center {
    left: 304px; width: 420px;
    background: radial-gradient(ellipse 62% 80% at 52% 45%, var(--magenta-glow) 0%, #b30b77 45%, var(--magenta-edge) 100%);
  }
  .banner--right  { left: 725px; width: 430px; }

  .ornament-area {
    position: absolute;
    background: linear-gradient(160deg, var(--ornament-tint) 0%, rgba(196, 70, 150, 0.10) 60%, rgba(196, 70, 150, 0) 100%);
  }
  .ornament-area--top-left   { left: 0;     top: 0;   width: 200px; height: 128px; }
  .ornament-area--lower-left { left: 114px; top: 110px; width: 167px; height: 179px; }
  .ornament-area--lower-mid  { left: 0;     top: 110px; width: 196px; height: 179px; }
  .ornament-area--right      { left: 115px; top: 0;   width: 315px; height: 198px; }

  .brand {
    position: absolute;
    left: 347px;
    top: 22px;
    width: 0;
    display: flex;
    flex-direction: column;
    align-items: center;
  }
  .brand__dot {
    width: 50px;
    height: 50px;
    border-radius: 50%;
    background: var(--logo-ink);
  }
  .brand__name {
    margin-top: 5px;
    font-family: "Quicksand", sans-serif;
    font-weight: 300;
    font-size: 15px;
    line-height: 18px;
    letter-spacing: 0.2px;
    color: var(--logo-ink);
    white-space: nowrap;
  }
</style>
</head>
<body>
<main class="sheet">
  <section class="banner banner--left">
    <div class="ornament-area ornament-area--top-left" role="img" aria-label="Faint decorative network pattern in light magenta"></div>
    <div class="ornament-area ornament-area--lower-left" role="img" aria-label="Faint decorative network pattern in light magenta"></div>
  </section>

  <section class="banner banner--center">
    <div class="ornament-area ornament-area--lower-mid" role="img" aria-label="Faint decorative network pattern in light magenta"></div>
    <div class="brand">
      <span class="brand__dot"></span>
      <span class="brand__name">BrightFold</span>
    </div>
  </section>

  <section class="banner banner--right">
    <div class="ornament-area ornament-area--right" role="img" aria-label="Faint decorative network pattern in light magenta"></div>
  </section>
</main>
</body>
</html>
```